BPH Business Card 2018

Brellmore Chiropractic. We have two locations that we want to advertise on the same card. Calderwick OrthoAxis campus address: 3815 Pemberly Dr., Suite 240, Thornbury, MS 39587. Ashcombe address: 426 Larkmoor Dr., Building D., Ashcombe, MS 39674. website: www.drbrellmore.example. o:(601)555-0148 f:(601)555-0173

Target Market(s)

Health care decision makers: primary care doctors and mothers

Contact Information for Business Card

I have no idea; up for any suggestions and I'd do much better picking from examples versus describing what I'm looking for. We are in a very high end location and would like the cards to look really sharp.

Requirements
Must have
• My name, Tobias R Venmark, D.C.

```html
<!DOCTYPE html>
<html lang="en">
<head>
<meta charset="utf-8">
<title>Brellmore Chiropractic Business Card</title>
<link rel="stylesheet" href="https://fonts.googleapis.com/css2?family=Merriweather:wght@400;700&display=swap">
<style>
  :root {
    --backdrop: #3a3a3c;
    --card: #232325;
    --card-edge: #3b3e42;
    --brand-blue: #0e5d86;
    --accent-blue: #1a7fc4;
    --ink-light: #f2f2f2;
    --ink-muted: #c9c9cb;
    --emboss: #38383b;
  }
  * { box-sizing: border-box; margin: 0; padding: 0; }
  html, body { width: 799px; height: 1200px; overflow: hidden; }
  body {
    background: var(--backdrop);
    font-family: "Merriweather", Georgia, serif;
    color: var(--ink-light);
    position: relative;
  }
  .card {
    position: absolute;
    left: 80px;
    width: 640px;
    height: 366px;
    background: var(--card);
    border-radius: 22px;
    overflow: hidden;
    box-shadow: 0 14px 30px rgba(0,0,0,.45);
  }
  .card--front { top: 150px; }
  .card--back { top: 660px; }

  /* Front */
  .front-wordmark {
    position: absolute; right: 50px; top: 44px;
    text-align: right; color: var(--emboss);
    font-weight: 700; text-transform: uppercase;
    line-height: 1.05;
  }
  .front-wordmark span { display: block; }
  .front-wordmark .w1 { font-size: 50px; letter-spacing: 2px; }
  .front-wordmark .w2 { font-size: 34px; letter-spacing: 3px; }
  .address-band {
    position: absolute; left: 0; right: 0; top: 172px; height: 100px;
    background: var(--brand-blue);
  }
  .campus-pill {
    position: absolute; left: 50%; top: 150px; transform: translateX(-50%);
    width: 230px; height: 46px;
    background: var(--card); border: 2px solid var(--ink-light);
    border-radius: 23px;
    display: flex; align-items: center; justify-content: center;
    font-weight: 700; font-size: 15px; z-index: 2;
  }
  .address {
    position: absolute; top: 212px;
    font-size: 13.5px; line-height: 1.45;
    display: flex; gap: 8px;
  }
  .address--west { left: 36px; }
  .address--east { right: 36px; text-align: right; }
  .address svg { width: 12px; height: 16px; flex: none; margin-top: 2px; }
  .band-divider {
    position: absolute; left: 50%; top: 204px; width: 1px; height: 54px;
    background: rgba(255,255,255,.45);
  }
  .front-web {
    position: absolute; left: 0; right: 0; top: 300px;
    display: flex; align-items: center; justify-content: center; gap: 18px;
    font-size: 15px;
  }
  .front-web .rule { width: 60px; height: 2px; background: var(--ink-light); }

  /* Back */
  .back-wordmark {
    position: absolute; left: 140px; top: 50px;
    color: var(--ink-light); font-weight: 400; text-transform: uppercase;
    display: flex; align-items: center; gap: 16px;
  }
  .back-wordmark .mark-dot {
    width: 22px; height: 22px; border-radius: 50%; background: var(--accent-blue); flex: none;
  }
  .back-wordmark .words { line-height: 1.05; }
  .back-wordmark .w1 { display: block; font-size: 44px; letter-spacing: 2px; color: var(--accent-blue); }
  .back-wordmark .w2 { display: block; font-size: 33px; letter-spacing: 3px; }
  .person { position: absolute; left: 38px; top: 212px; }
  .person-name { color: var(--accent-blue); font-size: 22px; }
  .person-title { color: var(--ink-muted); font-size: 12px; margin-top: 4px; }
  .contacts {
    position: absolute; left: 340px; top: 196px;
    list-style: none; font-size: 13.5px; line-height: 1.75;
  }
  .contacts li { display: flex; align-items: center; gap: 10px; }
  .contacts svg { width: 13px; height: 13px; flex: none; fill: var(--accent-blue); }
  .tagline-band { position: absolute; left: 0; bottom: 0; width: 640px; height: 80px; }
  .tagline {
    position: absolute; left: 300px; bottom: 26px;
    font-size: 16px; color: var(--ink-light);
  }
</style>
</head>
<body>

<section class="card card--front" aria-label="Card front">
  <div class="front-wordmark"><span class="w1">Brellmore</span><span class="w2">Chiropractic</span></div>
  <div class="address-band"></div>
  <div class="campus-pill">OrthoAxis Campus</div>
  <div class="address address--west">
    <svg viewBox="0 0 12 16"><path d="M6 0a6 6 0 0 0-6 6c0 4.5 6 10 6 10s6-5.5 6-10a6 6 0 0 0-6-6zm0 8.5A2.5 2.5 0 1 1 6 3.5a2.5 2.5 0 0 1 0 5z" fill="#f2f2f2"/></svg>
    <p>3815 Pemberly Dr., Suite 240,<br>Thornbury, AL 39587</p>
  </div>
  <div class="band-divider"></div>
  <div class="address address--east">
    <svg viewBox="0 0 12 16"><path d="M6 0a6 6 0 0 0-6 6c0 4.5 6 10 6 10s6-5.5 6-10a6 6 0 0 0-6-6zm0 8.5A2.5 2.5 0 1 1 6 3.5a2.5 2.5 0 0 1 0 5z" fill="#f2f2f2"/></svg>
    <p>426 Larkmoor Dr., Building D.,<br>Ashcombe, AL 39674</p>
  </div>
  <div class="front-web"><span class="rule"></span><span>www.drbrellmore.example</span><span class="rule"></span></div>
</section>

<section class="card card--back" aria-label="Card back">
  <div class="back-wordmark">
    <span class="mark-dot"></span>
    <span class="words"><span class="w1">Brellmore</span><span class="w2">Chiropractic</span></span>
  </div>
  <div class="person">
    <p class="person-name">Tobias R Venmark, D.C.</p>
    <p class="person-title">Managing Director</p>
  </div>
  <ul class="contacts">
    <li><svg viewBox="0 0 16 16"><path d="M3 1l3 3-2 2c1 2 4 5 6 6l2-2 3 3-2 2C7 15 1 9 1 3z"/></svg>(601)555-0148</li>
    <li><svg viewBox="0 0 16 16"><rect x="4" y="1" width="8" height="5"/><rect x="1" y="6" width="14" height="6" rx="1"/><rect x="4" y="11" width="8" height="4"/></svg>(601)555-0173</li>
    <li><svg viewBox="0 0 16 16"><path d="M1 3h14v10H1z M1 3l7 6 7-6" stroke="#232325" stroke-width="1.2"/></svg>t.r.venmark@drbrellmore.example</li>
    <li><svg viewBox="0 0 16 16"><circle cx="8" cy="8" r="7"/><path d="M1 8h14M8 1c-3 4-3 10 0 14M8 1c3 4 3 10 0 14" stroke="#232325" stroke-width="1" fill="none"/></svg>www.drbrellmore.example</li>
  </ul>
  <svg class="tagline-band" viewBox="0 0 640 80" aria-hidden="true">
    <path d="M0 60 L230 60 Q250 60 262 40 Q278 14 310 14 L640 14 L640 80 L0 80 Z" fill="#0e5d86"/>
    <path d="M0 60 L230 60 Q250 60 262 40 L262 80 L0 80 Z" fill="#3b3e42"/>
  </svg>
  <p class="tagline">Aligned For Life</p>
</section>

</body>
</html>
```